Sign Advertisment for Condominium Development

I need a sign created that will be placed in front of a building that is being converted into a luxury condominium development.

The sign needs to say:

Two, Boutique Luxury Condominiums Delivering late 2015.

Luxury Finishes // Designer Kitchens and Bath // Each Unit over 2,000 Square Feet

Deeded Parking Included with Each Unit

To Learn More, Contact:

Loretta Pinwell or Morgan Tesh
(202) 555-0147
Loretta.Pinwell@nrg-example.com

I need a small disclaimer at the bottom stating:

These Condominium(s) have not been registered by the Office of Residential Property Oversight Bureau of Dwelling Registration Tenancy Transfer and Purchase Section. A Condominium Unit may be reserved on a non-binding reservation agreement, but no contract of sale or lease that is binding on the purchaser may be entered into prior to registration.

Target Market(s)

Young professionals seeking luxury condominium

Industry/Entity Type

Building

Font styles to use
Serif

Colors
00a88f
ffffff

```html
<!DOCTYPE html>
<html lang="en">
<head>
<meta charset="utf-8">
<title>Boutique Luxury Condominiums – Sign</title>
<link rel="stylesheet" href="https://fonts.googleapis.com/css2?family=Open+Sans:ital,wght@0,400;0,700;1,400&family=PT+Serif:wght@400;700&family=Oswald:wght@500;600&display=swap">
<style>
  :root {
    --teal: #38bcae;
    --white: #ffffff;
    --ink: #1a1a1a;
    --partner: #2b3a55;
  }
  html, body {
    margin: 0;
    padding: 0;
    overflow: hidden;
    background: var(--white);
  }
  .sign {
    position: relative;
    width: 1200px;
    height: 927px;
    overflow: hidden;
    background: var(--white);
    color: var(--ink);
  }
  .sign__wave {
    position: absolute;
    inset: 0 0 auto 0;
    width: 1200px;
    height: 500px;
  }
  .headline-kicker,
  .headline-main,
  .status-list {
    position: absolute;
    margin: 0;
    color: var(--white);
    font-family: "Open Sans", sans-serif;
  }
  .headline-kicker {
    left: 52px;
    top: 34px;
    font-size: 70px;
    font-weight: 400;
    line-height: 1;
  }
  .headline-main {
    left: 144px;
    top: 120px;
    font-size: 122px;
    font-weight: 700;
    line-height: 1;
    letter-spacing: -1px;
  }
  .status-list {
    left: 666px;
    top: 262px;
    padding: 0;
    list-style: none;
    font-style: italic;
    font-size: 50px;
    line-height: 70px;
  }
  .status-list li::before {
    content: "";
    display: inline-block;
    width: 13px;
    height: 13px;
    margin-right: 18px;
    vertical-align: 10px;
    background: var(--white);
  }
  .feature-list {
    position: absolute;
    left: 50px;
    top: 360px;
    margin: 0;
    padding: 0;
    list-style: none;
    font-family: "PT Serif", serif;
    font-weight: 700;
    font-size: 38px;
    line-height: 83px;
  }
  .feature-list li::before {
    content: "";
    display: inline-block;
    width: 9px;
    height: 9px;
    margin-right: 14px;
    vertical-align: 8px;
    border-radius: 50%;
    background: var(--teal);
  }
  .contact {
    position: absolute;
    right: 52px;
    top: 494px;
    text-align: right;
    font-family: "Oswald", sans-serif;
    font-style: normal;
    font-weight: 600;
    color: var(--ink);
  }
  .contact__names {
    margin: 0;
    font-size: 36px;
    line-height: 46px;
  }
  .contact__phone {
    margin: 0;
    font-size: 98px;
    line-height: 112px;
    letter-spacing: -1px;
  }
  .contact__email {
    margin: 0;
    font-size: 40px;
    line-height: 54px;
  }
  .partners {
    position: absolute;
    left: 260px;
    top: 752px;
    width: 690px;
    display: flex;
    justify-content: space-between;
    align-items: center;
    font-family: "Oswald", sans-serif;
    font-weight: 500;
    font-size: 22px;
    color: var(--partner);
  }
  .partner {
    display: flex;
    align-items: center;
    gap: 8px;
  }
  .partner__mark {
    width: 14px;
    height: 14px;
    background: var(--partner);
  }
  .disclaimer {
    position: absolute;
    left: 52px;
    top: 826px;
    width: 1096px;
    margin: 0;
    font-family: "PT Serif", serif;
    font-size: 16px;
    line-height: 22px;
    text-align: justify;
    color: var(--ink);
  }
</style>
</head>
<body>
<main class="sign">
  <svg class="sign__wave" viewBox="0 0 1200 500" aria-hidden="true">
    <path d="M0,0 H1200 V488 C1000,488 820,480 700,430 C600,385 520,304 380,302 C260,300 120,330 0,362 Z" fill="var(--teal)"/>
  </svg>

  <h2 class="headline-kicker">Boutique Luxury</h2>
  <h1 class="headline-main">Condominiums</h1>

  <ul class="status-list">
    <li>Delivering late 2015</li>
    <li>2 units avail</li>
  </ul>

  <ul class="feature-list">
    <li>Luxury Finishes</li>
    <li>Designer Kitchen &amp; Bath</li>
    <li>Units over 2,000 sf</li>
    <li>Deeded Parking</li>
  </ul>

  <address class="contact">
    <p class="contact__names">Loretta Pinwell or Morgan Tesh</p>
    <p class="contact__phone">(202) 555-0147</p>
    <p class="contact__email">Loretta.Pinwell@nrg-example.com</p>
  </address>

  <div class="partners">
    <span class="partner"><span class="partner__mark"></span>Capitol Crest Properties</span>
    <span class="partner">Halvern Construction</span>
    <span class="partner"><span class="partner__mark"></span>Brightwater Bank</span>
  </div>

  <p class="disclaimer">These Condominium(s) have not been registered by the Office of Residential Property Oversight Bureau of Dwelling Registration Tenancy Transfer and Purchase Section. A Condominium Unit may be reserved on a non-binding reservation agreement, but no contract of sale or lease that is binding on the purchaser may be entered into prior to registration.</p>
</main>
</body>
</html>
```